" Hotel localizado na cidade de Fortaleza, próximo a rodoviária. Voltado para o público de negócios e com diferenciais importantes em relação aos demais hoteis da cidade, mais voltados ao turismo. Restaurante com diversas especialidades de pratos, com self-service e à lá carte. "

```html
<!DOCTYPE html>
<html lang="pt-BR">
<head>
<meta charset="utf-8">
<title>Hotel Terraluz</title>
<link rel="stylesheet" href="https://fonts.googleapis.com/css2?family=Bebas+Neue&family=Cinzel:wght@400&family=Arimo:wght@400;700&display=swap">
<style>
:root{
  --brown:#5a3a1e;
  --brown-dark:#2a1d17;
  --yellow:#f4d300;
  --sidebar:#f2f2f2;
  --panel:#ffffff;
  --grey-text:#9a9a9a;
  --line:#bdbdbd;
}
*{margin:0;padding:0;box-sizing:border-box}
html,body{width:1200px;height:952px;overflow:hidden}
body{position:relative;background:#e5e5e5;font-family:"Arimo",Arial,sans-serif}
.abs{position:absolute}
.backdrop{left:0;top:0}
.sidebar-shape{left:0;top:0}

/* brand */
.brand{left:142px;top:62px;width:228px;text-align:center;color:var(--brown);font-family:"Bebas Neue",sans-serif}
.brand-mark{display:block;width:78px;height:70px;margin:0 auto 8px;background:var(--yellow)}
.brand-small{font-size:15px;letter-spacing:14px;padding-left:14px;line-height:16px}
.brand-name{font-size:34px;letter-spacing:2px;line-height:34px}

/* navigation */
.nav{left:171px;top:210px;width:171px;list-style:none;border-top:2px solid var(--line)}
.nav li{height:33px;border-bottom:2px solid var(--line);font-family:"Bebas Neue",sans-serif;font-size:24px;line-height:34px;color:var(--brown);padding-left:3px}
.nav li.active{color:var(--yellow)}

/* booking */
.booking{left:142px;top:470px;width:228px;height:283px;background:linear-gradient(#5a4a3d,#2f241d)}
.booking h2{position:absolute;left:27px;top:32px;font-family:"Bebas Neue",sans-serif;font-weight:400;font-size:23px;color:#fff}
.booking .hint{position:absolute;left:27px;top:62px;font-size:11px;color:#8a7d72}
.booking label{position:absolute;font-size:11px;color:#fff;letter-spacing:-.2px}
.field{position:absolute;background:#fff;height:23px}
.small-field{position:absolute;background:#fff;width:23px;height:23px;font-size:11px;text-align:center;line-height:23px;color:#222}
.busca{position:absolute;left:143px;top:222px;width:68px;height:35px;background:var(--yellow);color:#fff;font-size:15px;text-align:center;line-height:35px}

.social{left:189px;top:768px;display:flex;gap:10px}
.social span{width:24px;height:24px;border-radius:50%;background:#8a8a8a}

/* main */
.main-shape{left:0;top:0}
.hero{left:419px;top:62px}
.hero-title{left:626px;top:114px;width:401px;height:32px;background:rgba(40,28,20,.7);color:#fff;font-family:"Bebas Neue",sans-serif;font-size:25px;line-height:32px;padding-left:5px}
.hero-text{left:626px;top:157px;width:401px;height:65px;background:rgba(40,28,20,.7);color:#fff;font-family:"Bebas Neue",sans-serif;font-size:17.5px;line-height:21.5px;padding:2px 6px}
.hero-text em{font-style:normal;color:var(--yellow)}

.card{width:294px;height:114px;background:linear-gradient(100deg,#3d2e28,#251a16 60%,#3a2b25)}
.card .ribbon{position:absolute;left:13px;top:0}
.card h3{position:absolute;left:50px;top:26px;font-family:"Cinzel",serif;font-weight:400;font-size:21px;color:#fff;letter-spacing:.5px}
.card p{position:absolute;left:53px;top:58px;width:240px;font-size:10.5px;line-height:13px;color:#c8a800}
.card .more{position:absolute;left:174px;top:70px;width:84px;height:28px;background:#3b2d27;color:#e8e0d8;font-family:"Cinzel",serif;font-size:12px;letter-spacing:1px;text-align:center;line-height:28px}

.divider{left:422px;top:537px;width:610px;height:1px;background:#cfcfcf}
.section-title{font-family:"Bebas Neue",sans-serif;font-size:25px;color:var(--brown);font-weight:400}

.news{left:418px;width:260px;display:flex;gap:7px}
.news .date{width:40px;height:42px;border:1px solid #cfcfcf;border-radius:8px;color:var(--yellow);font-size:17px;line-height:15px;text-align:center;padding-top:6px;flex:none}
.news p{font-size:10.5px;line-height:13.7px;color:var(--grey-text);margin-top:-3px}

.map{left:737px;top:635px}
.footer{left:389px;top:903px;width:666px;text-align:center;font-family:"Cinzel",serif;font-size:15px;color:#555;letter-spacing:.5px}
</style>
</head>
<body>

<svg class="abs backdrop" width="1200" height="952" viewBox="0 0 1200 952" role="img" aria-label="Foto desfocada de um quarto do hotel ao fundo">
  <defs>
    <linearGradient id="room" x1="0" y1="0" x2="1" y2="0.4">
      <stop offset="0" stop-color="#b8352a"/>
      <stop offset=".35" stop-color="#d9a18f"/>
      <stop offset=".6" stop-color="#c43a2d"/>
      <stop offset="1" stop-color="#a82a22"/>
    </linearGradient>
  </defs>
  <rect width="1200" height="952" fill="#e4e4e4"/>
  <path d="M0,0 H1200 V505 Q600,570 0,480 Z" fill="url(#room)"/>
  <path d="M0,480 Q600,570 1200,505 V660 Q600,700 0,650 Z" fill="#f1f1f1"/>
</svg>

<svg class="abs sidebar-shape" width="1200" height="952" aria-hidden="true">
  <path d="M142,62 Q256,48 370,38 L370,878 Q256,866 142,857 Z" fill="#f2f2f2"/>
</svg>

<svg class="abs main-shape" width="1200" height="952" aria-hidden="true">
  <path d="M389,38 Q720,22 1055,58 L1055,855 Q720,895 389,887 Z" fill="#fff"/>
</svg>

<aside>
  <div class="abs brand">
    <span class="brand-mark"></span>
    <div class="brand-small">HOTEL</div>
    <div class="brand-name">TERRALUZ</div>
  </div>

  <ul class="abs nav">
    <li class="active">Home</li>
    <li>Hotel</li>
    <li>Quartos</li>
    <li>Serviços</li>
    <li>Blog</li>
    <li>Contatos</li>
  </ul>

  <form class="abs booking">
    <h2>Reservar um quarto</h2>
    <span class="hint">Informações de reserva:</span>
    <label style="left:27px;top:94px">Entrada</label>
    <span class="field" style="left:26px;top:109px;width:57px"></span>
    <span class="field" style="left:90px;top:109px;width:117px"></span>
    <label style="left:27px;top:141px">Saida</label>
    <span class="field" style="left:26px;top:157px;width:57px"></span>
    <span class="field" style="left:90px;top:157px;width:117px"></span>
    <label style="left:43px;top:196px">Pessoas</label>
    <span class="small-field" style="left:90px;top:185px">2</span>
    <label style="left:128px;top:196px">Quartos</label>
    <span class="small-field" style="left:171px;top:187px">3</span>
    <span class="busca">busca</span>
  </form>

  <div class="abs social"><span></span><span></span><span></span><span></span></div>
</aside>

<main>
  <svg class="abs hero" width="609" height="308" viewBox="0 0 609 308" role="img" aria-label="Foto de quarto com cama de dossel e parede amarela">
    <defs>
      <linearGradient id="heroFill" x1="0" y1="0" x2="1" y2="1">
        <stop offset="0" stop-color="#e0b040"/>
        <stop offset=".45" stop-color="#a86a2a"/>
        <stop offset="1" stop-color="#4a2c16"/>
      </linearGradient>
    </defs>
    <path d="M0,2 Q300,-6 609,26 V308 H0 Z" fill="url(#heroFill)"/>
  </svg>
  <div class="abs hero-title">Lorem ipsum dolor sit amet, consectetur</div>
  <div class="abs hero-text">Lorem ipsum dolor sit amet, consectetur adipiscing elit. Sed ut congue ipsum. Phasellus a felis a <em>massa commodo</em> sollicitudin a sagittis lorem.</div>

  <article class="abs card" style="left:419px;top:396px">
    <svg class="ribbon" width="28" height="70" aria-hidden="true"><path d="M0,0 H28 V70 L14,62 L0,70 Z" fill="#e2d400"/></svg>
    <h3>REUNIÕES E EVENTOS</h3>
    <p>is simply dummy text of the printing and typesetting industry. Lorem Ipsum</p>
    <span class="more">LEIA MAIS</span>
  </article>
  <article class="abs card" style="left:734px;top:396px">
    <svg class="ribbon" width="28" height="70" aria-hidden="true"><path d="M0,0 H28 V70 L14,62 L0,70 Z" fill="#e2d400"/></svg>
    <h3>REUNIÕES E EVENTOS</h3>
    <p>is simply dummy text of the printing and typesetting industry. Lorem Ipsum</p>
    <span class="more">LEIA MAIS</span>
  </article>

  <div class="abs divider"></div>

  <h2 class="abs section-title" style="left:422px;top:578px">Noticias</h2>
  <h2 class="abs section-title" style="left:736px;top:580px">Onde estamos</h2>

  <div class="abs news" style="top:614px">
    <div class="date">04<br>abr</div>
    <p>Consectetur Adipiscing Elit<br>Lorem ipsum dolor sit amet,<br>consectetur adipiscing elit. Pellentesque<br>non eleifend tellus. Ut dui ve...</p>
  </div>
  <div class="abs news" style="top:697px">
    <div class="date">04<br>abr</div>
    <p>Consectetur Adipiscing Elit<br>Lorem ipsum dolor sit amet,<br>consectetur adipiscing elit. Pellentesque<br>non eleifend tellus. Ut dui ve...</p>
  </div>
  <div class="abs news" style="top:775px">
    <div class="date">04<br>abr</div>
    <p>Consectetur Adipiscing Elit<br>Lorem ipsum dolor sit amet,<br>consectetur adipiscing elit. Pellentesque<br>non eleifend tellus. Ut dui ve...</p>
  </div>

  <svg class="abs map" width="288" height="144" viewBox="0 0 288 144" role="img" aria-label="Mapa de satélite da localização do hotel perto da rodoviária">
    <defs>
      <linearGradient id="mapFill" x1="0" y1="0" x2="1" y2="1">
        <stop offset="0" stop-color="#6f7f5e"/>
        <stop offset=".5" stop-color="#8e948a"/>
        <stop offset="1" stop-color="#5d6a50"/>
      </linearGradient>
    </defs>
    <rect width="288" height="144" fill="url(#mapFill)"/>
  </svg>
</main>

<footer class="abs footer">© 2013 Todos direitos reservados</footer>

</body>
</html>
```